Fun Employee News and Engagement Portal - Brisk Oven Company

We are looking for a clean, but fun WordPress template for an internal employee engagement website. The site will be a place we share news, fun stories and pictures. We'll provide space for our employees to post comments, etc.
We are a deep dish pizza restaurant with a rich history. I'd love to see your take on a look and feel for us! The site will be called Bam-Zee. I've posted some images and colors along with this brief description.
Focus on making the template whimsical and fun! (Extra point for focusing on the "Lettering in lights" ).
I will continue to post additional pieces of art and content examples.
Reason: Our team is continuing to review designs. We've decided to extend the timing a few more days. Good luck! Make it playful!
Reason: We need more time with our team to review these designs. We are going to extend one more time!
Reason: Still trying to get enough time to review with the Bam-Zee team!
Reason: We are continuing to evaluate designs. Thank you!

```html
<!DOCTYPE html>
<html lang="en">
<head>
<meta charset="UTF-8">
<title>Disserendum valet</title>
<link href="https://fonts.googleapis.com/css2?family=Playfair+Display:wght@400&family=Open+Sans:wght@400;600;700&display=swap" rel="stylesheet">
<style>
  :root {
    --brand-red: #e91e26;
    --panel-white: #ffffff;
    --ink: #1a1a1a;
    --body-text: #4a4a4a;
    --meta-text: #8a8a8a;
    --button-dark: #1c1c1e;
    --link-teal: #6fb7c0;
    --photo-warm: #e89a3c;
    --photo-deep: #c2541c;
    --photo-light: #f4c65a;
  }
  * { margin: 0; padding: 0; box-sizing: border-box; }
  html, body {
    width: 1200px;
    height: 1200px;
    overflow: hidden;
    background: var(--brand-red);
  }
  .canvas {
    position: relative;
    width: 1200px;
    height: 1200px;
    background: var(--brand-red);
    font-family: "Open Sans", sans-serif;
  }
  .post-panel {
    position: absolute;
    left: 0;
    top: 0;
  }
  .post-title {
    position: absolute;
    top: 64px;
    left: 92px;
    width: 1028px;
    text-align: center;
    font-family: "Playfair Display", serif;
    font-weight: 400;
    font-size: 35px;
    color: var(--ink);
  }
  .post-meta {
    position: absolute;
    top: 119px;
    left: 92px;
    width: 1028px;
    text-align: center;
    font-size: 10.5px;
    color: var(--meta-text);
    word-spacing: 1px;
  }
  .post-meta .sep { margin: 0 6px; }
  .post-photo {
    position: absolute;
    left: 146px;
    top: 162px;
    width: 920px;
    height: 596px;
    background:
      radial-gradient(ellipse at 60% 55%, var(--photo-light) 0%, transparent 55%),
      linear-gradient(160deg, #8a8c94 0%, #8a8c94 12%, var(--photo-warm) 26%, var(--photo-deep) 65%, #b9692e 100%);
  }
  .post-excerpt {
    position: absolute;
    left: 146px;
    top: 785px;
    width: 906px;
    font-size: 13px;
    line-height: 22px;
    color: var(--body-text);
  }
  .tag-button {
    position: absolute;
    left: 92px;
    top: 1030px;
    width: 119px;
    height: 47px;
    background: var(--button-dark);
    color: #ffffff;
    font-size: 13px;
    line-height: 47px;
    text-align: center;
  }
  .reply-heading {
    position: absolute;
    left: 92px;
    top: 1113px;
    font-family: "Playfair Display", serif;
    font-weight: 400;
    font-size: 22px;
    color: #ffffff;
  }
  .reply-status {
    position: absolute;
    left: 92px;
    top: 1150px;
    font-size: 13px;
    color: var(--link-teal);
  }
  .comment-label {
    position: absolute;
    left: 92px;
    top: 1181px;
    font-size: 13px;
    font-weight: 700;
    color: #ffffff;
  }
</style>
</head>
<body>
<div class="canvas">
  <svg class="post-panel" width="1200" height="1200" viewBox="0 0 1200 1200" aria-hidden="true">
    <polygon points="92,14 304,0 1120,0 1120,894 92,974" fill="var(--panel-white)"/>
  </svg>

  <h1 class="post-title">Disserendum valet</h1>
  <p class="post-meta">February 22, 2017<span class="sep">/</span>admin<span class="sep">/</span>News</p>

  <div class="post-photo" role="img" aria-label="Close-up photo of a pizza with olives, corn, peppers and stretching melted cheese"></div>

  <p class="post-excerpt">Lorem ipsum dolor sit amet, consectetur adipiscing elit. Non enim solum Torquatus dixit quid sentiret, sed etiam cur. Immo alio genere; Omnes<br>enim iucundum motum, quo sensus hilaretur. Ut in geometria, prima si dederis, danda[...]</p>

  <div class="tag-button">Nullam dictum</div>

  <h2 class="reply-heading">Leave a Reply</h2>
  <p class="reply-status">Logged in as admin. Log out?</p>
  <p class="comment-label">Comment</p>
</div>
</body>
</html>
```